Harrowgate Properties Needs New Stationery Design

We need new clean and white stationery for our property management company based in Winnipeg, Manitoba, Canada. We manage condominium and commercial properties. Additionally, we do real estate development and commercial leasing.

We'll require the following:
- Business cards
- Letterhead*
- Envelope (we mainly use #10, single window envelope)
- Fax Cover Sheet
- *Electronic version of the letterhead that works in Google Docs (.jpg for top header)

Industry/Entity Type

Property Management

```html
<!DOCTYPE html>
<html lang="en">
<head>
<meta charset="utf-8">
<title>Harrowgate Properties Stationery</title>
<link href="https://fonts.googleapis.com/css2?family=Oswald:wght@600&family=Open+Sans:wght@400;700&display=swap" rel="stylesheet">
<style>
:root{
  --navy:#283f73;
  --cyan:#1ba6cf;
  --grey-text:#6b6b6b;
  --grey-band:#e3e3e3;
  --board:#000;
  --paper:#fff;
  --card-light:#a9d8ef;
  --card-mid:#5fb4e0;
}
*{margin:0;padding:0;box-sizing:border-box}
html,body{width:1200px;height:992px;overflow:hidden;background:var(--board)}
.board{position:absolute;left:0;top:0;width:1154px;height:956px;transform-origin:0 0;transform:scale(1.0399,1.0377);font-family:"Open Sans",Arial,sans-serif}
.wordmark{font-family:"Oswald","Arial Narrow",sans-serif;font-weight:600;color:var(--navy);line-height:.95;text-align:right;position:absolute}
.wordmark .sub{display:block;letter-spacing:.08em}

/* letterhead */
.letterhead{position:absolute;left:83px;top:55px;width:595px;height:842px;background:var(--paper)}
.letterhead-header{position:absolute;left:0;top:0;width:595px;height:103px}
.letterhead-band{position:absolute;left:0;top:103px;width:595px;height:21px;background:var(--grey-band);border-bottom:1px solid #c9c9c9;color:#8a8a8a;font-size:14px;font-weight:700;letter-spacing:.06em;text-align:center;line-height:21px}
.letterhead .wordmark{left:215px;top:35px;width:160px;font-size:30px}
.letterhead .wordmark .sub{font-size:12px}
.letterhead-footer{position:absolute;left:0;top:786px;width:595px;text-align:center;font-size:10.5px;line-height:13px;color:var(--grey-text)}
.letterhead-rule{position:absolute;left:39px;top:818px;width:517px;border-top:3px dotted #9a9a9a}

/* business cards */
.card{position:absolute;left:27px;width:189px;height:109px;border-radius:6px;border:3px solid #c7c9cc;background:radial-gradient(circle at 45% 60%,var(--card-light),var(--card-mid) 75%);overflow:hidden}
.card-front{top:380px}
.card-back{top:510px}
.card-name{position:absolute;left:8px;top:12px;color:#fff;font-size:12.5px}
.card-name b{font-weight:700}
.card-title-strip{position:absolute;left:0;top:28px;width:100%;height:10px;background:rgba(255,255,255,.35);font-size:6.5px;color:rgba(255,255,255,.75);padding-left:88px;line-height:10px}
.card .wordmark{right:14px;font-size:16px}
.card .wordmark .sub{font-size:6.5px}
.card-front .wordmark{top:56px}
.card-back .wordmark{top:56px}
.card-contact{position:absolute;left:3px;top:8px;font-size:5px;line-height:6.3px;color:#fff}
.card-social{position:absolute;left:105px;top:15px;display:flex;gap:8px}
.card-social span{width:10px;height:10px;border-radius:2px;background:var(--navy);opacity:.8}
.card-web-strip{position:absolute;left:0;top:88px;width:100%;height:11px;background:rgba(255,255,255,.35);font-size:6.5px;color:rgba(40,63,115,.6);text-align:center;line-height:11px}

/* envelope */
.envelope{position:absolute;left:466px;top:484px;width:655px;height:313px;background:var(--paper)}
.envelope-band{position:absolute;left:0;bottom:0;width:100%;height:37px;background:var(--navy)}
.envelope .wordmark{right:20px;top:104px;font-size:40px}
.envelope .wordmark .sub{font-size:15px}
.envelope-address{position:absolute;left:11px;top:203px;font-size:10px;line-height:13.2px;color:var(--grey-text)}

/* disc label */
.disc{position:absolute;left:0;top:0;width:1154px;height:956px}
.disc-mark{position:absolute;left:615px;top:262px;width:130px;font-size:31px}
.disc-mark .sub{font-size:11px}
</style>
</head>
<body>
<main class="board">

  <section class="letterhead">
    <svg class="letterhead-header" viewBox="0 0 595 103" aria-hidden="true">
      <defs>
        <pattern id="stripes" width="4" height="4" patternUnits="userSpaceOnUse">
          <rect width="4" height="4" fill="#d9d9d9"/>
          <rect width="4" height="2" fill="#c4c4c4"/>
        </pattern>
      </defs>
      <rect width="595" height="103" fill="url(#stripes)"/>
      <path d="M0 14 C120 10 200 80 310 84 C420 88 480 30 595 18 L595 103 L0 103 Z" fill="var(--navy)"/>
      <path d="M0 22 C120 18 200 88 310 92 C420 96 480 38 595 26" fill="none" stroke="#fff" stroke-width="2"/>
      <ellipse cx="290" cy="0" rx="100" ry="24" fill="#fff"/>
      <rect x="0" y="14" width="595" height="1" fill="#fff" opacity=".5"/>
    </svg>
    <div class="wordmark">Harrowgate<span class="sub">PROPERTIES</span></div>
    <div class="letterhead-band">HARROWGATE PROPERTIES CORP</div>
    <p class="letterhead-footer">Harrowgate Properties Corp. 412 Elm Crescent Winnipeg, MB R2K 4T1.<br>Tel (204) 555-0142, Fax (204) 555-0143 info@harrowgateproperties.ca, www.harrowgateproperties.ca</p>
    <div class="letterhead-rule"></div>
  </section>

  <section class="card card-front">
    <p class="card-name"><b>Martin</b> Keller</p>
    <div class="card-title-strip">President &amp; CEO</div>
    <div class="wordmark">Harrowgate<span class="sub">PROPERTIES</span></div>
  </section>

  <section class="card card-back">
    <p class="card-contact">Harrowgate Properties Corp.<br>412 Elm Crescent Winnipeg,<br>MB R2K 4T1<br>Tel (204) 555-0142<br>Fax (204) 555-0143<br>info@harrowgateproperties.ca</p>
    <div class="card-social"><span></span><span></span><span></span><span></span></div>
    <div class="wordmark">Harrowgate<span class="sub">PROPERTIES</span></div>
    <div class="card-web-strip">www.harrowgateproperties.ca</div>
  </section>

  <section class="envelope">
    <div class="wordmark">Harrowgate<span class="sub">PROPERTIES</span></div>
    <p class="envelope-address">Harrowgate Properties Corp.<br>412 Elm Crescent Winnipeg,&nbsp; MB R2K 4T1.<br>Tel (204) 555-0142, Fax (204) 555-0143<br>info@harrowgateproperties.ca,<br>www.harrowgateproperties.ca</p>
    <div class="envelope-band"></div>
  </section>

  <svg class="disc" viewBox="0 0 1154 956" aria-hidden="true">
    <circle cx="694" cy="392" r="170" fill="var(--navy)" stroke="#000" stroke-width="1"/>
    <circle cx="685" cy="387" r="169" fill="#fff"/>
    <circle cx="677" cy="383" r="168" fill="var(--navy)"/>
    <circle cx="668" cy="378" r="168" fill="#fff" stroke="#000" stroke-width="1"/>
    <circle cx="682" cy="378" r="53" fill="#fff" stroke="#555" stroke-width=".7"/>
    <path d="M682 325 A53 53 0 0 1 682 431 Z" fill="#000"/>
  </svg>
  <div class="wordmark disc-mark">Harrowgate<span class="sub">PROPERTIES</span></div>

</main>
</body>
</html>
```